new construction company branding

branding

Can I have a banner made so I can hang it as 1) branding my jobsite 2) advertisement

Target Market(s)

Commercial

Industry/Entity Type

Construction Trade

Font styles to use
Other font styles liked:
• Cinzel bold

Colors
EB3D1F
EC4F4E
F09395
F8D3D4
FCEDEE

Requirements
Must have
• Bright colors for advertisement
Nice to have
• 36”x48” canvas
Should not have
• To busy

```html
<!DOCTYPE html>
<html lang="en">
<head>
<meta charset="utf-8">
<title>Ridgeline Build Co — Jobsite Banner</title>
<link href="https://fonts.googleapis.com/css2?family=Montserrat:wght@400;500;600;700;800&display=swap" rel="stylesheet">
<style>
  :root {
    --red: #e20f12;
    --ink: #1d1d1d;
    --white: #ffffff;
    --paper: #ffffff;
    --mist: #e4e4e4;
  }
  html, body {
    margin: 0;
    padding: 0;
    width: 1200px;
    height: 720px;
    overflow: hidden;
    background: #d0d0d0;
  }
  .banner {
    position: relative;
    width: 1200px;
    height: 720px;
    background: var(--paper);
    overflow: hidden;
    font-family: "Montserrat", sans-serif;
  }
  .texture {
    position: absolute;
    right: 0;
    top: 0;
    width: 560px;
    height: 420px;
    background: radial-gradient(ellipse at 75% 35%, #d9d9d9 0%, #ececec 40%, rgba(255,255,255,0) 75%);
  }
  .shapes {
    position: absolute;
    inset: 0;
  }
  .headline {
    position: absolute;
    left: 21px;
    top: 30px;
    margin: 0;
    font-weight: 800;
    line-height: 1;
  }
  .headline-top {
    display: block;
    color: var(--red);
    font-size: 91px;
    letter-spacing: 0.5px;
  }
  .headline-bottom {
    display: block;
    color: var(--ink);
    font-size: 72px;
    font-weight: 500;
    margin-top: 14px;
    letter-spacing: 1px;
  }
  .trade {
    position: absolute;
    left: 24px;
    top: 270px;
    margin: 0;
    color: var(--ink);
    font-size: 41px;
    font-weight: 500;
    letter-spacing: 1.5px;
  }
  .credentials {
    position: absolute;
    left: 23px;
    top: 330px;
    margin: 0;
    color: var(--red);
    font-size: 32px;
    font-weight: 500;
    line-height: 43px;
  }
  .phone {
    position: absolute;
    left: 17px;
    top: 598px;
    display: flex;
    align-items: center;
    gap: 8px;
    color: var(--white);
    font-size: 53px;
    font-weight: 700;
    letter-spacing: 0.5px;
  }
  .website {
    position: absolute;
    left: 16px;
    top: 676px;
    display: flex;
    align-items: center;
    gap: 7px;
    color: var(--white);
    font-size: 16px;
    font-weight: 600;
  }
  .brand {
    position: absolute;
    left: 700px;
    width: 490px;
    top: 588px;
    text-align: center;
  }
  .brand-name {
    margin: 0;
    color: var(--white);
    font-size: 34px;
    font-weight: 700;
    letter-spacing: 1px;
  }
  .brand-tagline {
    margin: 8px 0 0;
    color: var(--red);
    font-size: 22px;
    font-weight: 700;
    letter-spacing: 9px;
  }
</style>
</head>
<body>
  <main class="banner">
    <div class="texture" role="img" aria-label="Soft grey geometric triangle texture"></div>

    <svg class="shapes" width="1200" height="720" viewBox="0 0 1200 720" aria-hidden="true">
      <path class="brand-panel" d="M605 720 C 760 480, 980 360, 1200 339 L1200 720 Z" fill="var(--ink)"/>
      <line class="rule" x1="34" y1="236" x2="661" y2="236" stroke="var(--red)" stroke-width="1.5"/>
      <polygon class="rule-mark" points="322,218 395,218 371,250 298,250" fill="var(--ink)"/>
      <polygon class="phone-band" points="0,600 441,600 375,666 0,666" fill="var(--red)"/>
      <polygon class="web-band" points="0,666 297,666 260,709 0,709" fill="var(--ink)"/>
    </svg>

    <h1 class="headline">
      <span class="headline-top">TOGETHER ACHIEVING</span>
      <span class="headline-bottom">COMMAN GOALS</span>
    </h1>

    <p class="trade">GENERAL CONTRACTOR</p>

    <p class="credentials">License b no #2048731<br>Bonded/insured</p>

    <div class="phone">
      <svg width="18" height="32" viewBox="0 0 18 32" aria-hidden="true">
        <rect x="1.5" y="1.5" width="15" height="29" rx="2.5" fill="none" stroke="var(--white)" stroke-width="3"/>
        <rect x="4" y="5" width="10" height="20" fill="var(--red)"/>
      </svg>
      <span>123-4567-890</span>
    </div>

    <div class="website">
      <svg width="13" height="13" viewBox="0 0 14 14" aria-hidden="true">
        <circle cx="7" cy="7" r="6" fill="none" stroke="var(--white)" stroke-width="1.4"/>
        <ellipse cx="7" cy="7" rx="2.6" ry="6" fill="none" stroke="var(--white)" stroke-width="1.2"/>
        <line x1="1" y1="7" x2="13" y2="7" stroke="var(--white)" stroke-width="1.2"/>
      </svg>
      <span>www.yourwebsiet.com</span>
    </div>

    <div class="brand">
      <p class="brand-name">RIDGELINE BUILD CO</p>
      <p class="brand-tagline">GENERAL CONTRACTOR</p>
    </div>
  </main>
</body>
</html>
```